Wordpress template re-design of current website

We need a WordPress template design and new look for our existing website. Our existing site it located at www.velmoro.com.au We are a tech company and want a fresh, clean modern website that matches our brand, services and logo colors. Our main Services are hospitality solutions, Velmoro TV solution and managed networks, more information on these can come from our existing website.

Target Market(s)

We are a tech company so must have a modern feel for new technology

Industry/Entity Type

It Company

Number of Pages Required

5+ page

Font styles to use
Sans Serif

Requirements
Must have
• Be based on a wordpress templete design and match the services that we have in our existing website, in the testimonials want a place for video testimonials as well as text. Nice clean icons used for graphics to represent services.
Nice to have
• nice visual representation of our services in the way of clean icons etc
Should not have
• Clutter

```html
<!DOCTYPE html>
<html lang="en">
<head>
<meta charset="utf-8">
<title>Velmoro Wireless – About Us</title>
<link rel="stylesheet" href="https://fonts.googleapis.com/css2?family=Roboto+Condensed:wght@400;700&family=Open+Sans:wght@400;600&display=swap">
<style>
:root{
  --brand:#1d4f8c;
  --brand-dark:#0f3a70;
  --heading:#1a4a86;
  --text:#555b62;
  --muted:#8a9098;
  --icon:#5f6d7c;
  --dark:#1f2226;
  --light:#f6f7f8;
  --footer:#0e3c74;
  --bar:#2b2b2b;
  --white:#ffffff;
}
*{margin:0;padding:0;box-sizing:border-box}
html,body{width:1200px;height:2419px;overflow:hidden}
body{position:relative;background:var(--white);font-family:"Open Sans",Arial,sans-serif;color:var(--text)}
.abs{position:absolute}
.cond{font-family:"Roboto Condensed","Arial Narrow",sans-serif}

/* header */
.site-header{left:0;top:0;width:1200px;height:98px;border-top:3px solid var(--brand-dark);background:var(--white)}
.logo{left:100px;top:22px;display:flex;align-items:center;gap:10px}
.logo-name{font-family:"Roboto Condensed",sans-serif;font-weight:700;font-size:40px;color:var(--brand)}
.logo-dot{width:26px;height:26px;border-radius:50%;background:var(--brand)}
.main-nav{left:388px;top:34px;display:flex;gap:10px;white-space:nowrap}
.main-nav a{font-family:"Roboto Condensed",sans-serif;font-size:14px;color:#555;text-decoration:none;padding:7px 14px;border:1.5px solid transparent;border-radius:4px;letter-spacing:.5px}
.main-nav a.active{border-color:var(--brand);color:var(--brand)}
.header-divider{left:893px;top:18px;width:1px;height:62px;background:#e3e3e3}
.header-contact{right:142px;top:28px;text-align:right;white-space:nowrap;font-size:14px;line-height:21px;color:var(--brand-dark)}
.phone-ring{left:1068px;top:32px;width:34px;height:34px;border:2px solid var(--brand-dark);border-radius:50%}

/* hero */
.hero{left:0;top:98px;width:1200px;height:178px;background:linear-gradient(180deg,#2e5f9c,#3a6ca8 60%,#2a578f)}
.hero h1{width:100%;top:70px;text-align:center;font-size:52px;font-weight:700;color:var(--white)}

/* about */
.section-title{left:98px;top:310px;font-size:31px;font-weight:400;color:var(--heading);letter-spacing:.5px}
.photo{left:98px;top:374px;width:392px;height:254px;border:3px solid var(--brand);background:linear-gradient(160deg,#6aa7d8 0%,#9cc8e4 40%,#c7b08a 75%,#a88a62 100%)}
.intro{left:98px;top:648px;width:398px;font-size:11.5px;line-height:23px;text-align:justify}
.intro p+p{margin-top:10px}
.feature{left:546px;width:557px}
.feature-head{display:flex;align-items:center;gap:18px;margin-bottom:14px}
.icon-circle{width:50px;height:50px;border-radius:50%;background:var(--icon);flex:none;display:flex;align-items:center;justify-content:center}
.feature-title{font-size:20px;color:#55606b;line-height:25px;font-weight:400}
.feature p{font-size:11.3px;line-height:20px;text-align:justify;margin-bottom:8px}
.philosophy{left:98px;top:862px;width:1005px}
.philosophy p{font-size:11.2px;line-height:20px;margin-bottom:10px}

/* statement band */
.statement{left:0;top:1145px;width:1200px;height:335px;background:radial-gradient(ellipse at 50% 40%,#3a3d42,#1b1d20 75%)}
.statement h2{top:100px;width:100%;text-align:center;font-size:50px;font-weight:700;color:var(--white);letter-spacing:.5px}
.statement p{top:168px;width:100%;text-align:center;font-size:25px;line-height:32px;color:#eee}

/* team */
.team{left:0;top:1480px;width:1200px;height:523px;background:var(--light)}
.team h2{top:38px;width:100%;text-align:center;font-size:34px;color:var(--heading);font-weight:400}
.team .sub{top:80px;width:100%;text-align:center;font-size:15px;color:var(--brand)}
.team .rule{top:111px;left:570px;width:60px;height:1px;background:#cfd4da}
.card{top:156px;width:235px;height:304px;background:var(--white);box-shadow:0 1px 4px rgba(0,0,0,.18);overflow:hidden}
.card-top{position:absolute;left:0;top:0;width:235px;height:90px;background:linear-gradient(180deg,#3d6fab,#5e8cc2)}
.card-cut{position:absolute;left:0;top:0}
.avatar{position:absolute;left:60px;top:26px;width:116px;height:116px;border-radius:50%;border:4px solid var(--white);background:linear-gradient(180deg,#d9dde2,#9aa6b4);box-shadow:0 1px 3px rgba(0,0,0,.25)}
.card h3{position:absolute;top:170px;width:100%;text-align:center;font-family:"Roboto Condensed",sans-serif;font-size:18px;font-weight:400;color:var(--brand-dark)}
.card p{position:absolute;top:196px;left:20px;width:195px;text-align:center;font-size:11.5px;line-height:21px;color:#444}
.card .socials{position:absolute;top:268px;width:100%;display:flex;justify-content:center;gap:3px}
.card .socials span{width:12px;height:12px;background:#555;border-radius:2px}

/* partners */
.partners{left:0;top:2003px;width:1200px;height:137px;border-top:1px solid #e6e6e6}
.partner{top:33px;width:155px;height:74px;border:1px solid #e4e4e4;background:var(--white);display:flex;align-items:center;justify-content:center}
.partner span{width:90px;height:26px;border-radius:4px;background:#d9dde2}

/* footer */
.site-footer{left:0;top:2140px;width:1200px;height:228px;background:linear-gradient(180deg,#0f3f79,#0b3569)}
.foot-logo{left:100px;top:58px;display:flex;align-items:center;gap:8px}
.foot-logo .logo-name{color:var(--white);font-size:36px}
.foot-logo .logo-dot{background:var(--white);width:22px;height:22px}
.foot-social{left:114px;top:138px;display:flex;gap:6px}
.foot-social span{width:25px;height:25px;border:1px solid #cfd8e4;border-radius:50%}
.foot-head{font-size:17px;color:var(--white);letter-spacing:.5px}
.foot-links{left:329px;top:42px}
.foot-links ul{list-style:none;margin-top:22px}
.foot-links li{font-size:12px;color:#e3ebf5;line-height:24px}
.foot-contact{left:516px;top:42px}
.contact-row{display:flex;align-items:flex-start;gap:14px;color:#e8eef6;font-size:13px;line-height:20px;margin-top:18px}
.contact-row svg{flex:none;margin-top:2px}
.signup{left:832px;top:40px}
.field{width:271px;height:40px;border:1px solid #2a5590;background:#0c3466;color:#e8eef6;font-size:11px;padding:13px 14px;margin-top:14px}
.field.email{width:174px;display:inline-block}
.btn{display:inline-block;width:97px;height:40px;background:var(--dark);color:var(--white);font-size:12px;text-align:center;line-height:40px;vertical-align:top;margin-top:14px}
.copyright{left:0;top:2368px;width:1200px;height:51px;background:var(--bar);color:#ddd;font-size:12px;text-align:center;line-height:51px}
</style>
</head>
<body>

<header class="abs site-header">
  <div class="abs logo"><span class="logo-name">Velmoro</span><span class="logo-dot"></span></div>
  <nav class="abs main-nav">
    <a href="#">HOME</a><a href="#" class="active">ABOUT US</a><a href="#">SERVICES</a><a href="#">OUR WORK</a><a href="#">CONTACT</a>
  </nav>
  <div class="abs header-divider"></div>
  <div class="abs header-contact">+1 1300 555 014<br>info@velmoro.com.au</div>
  <div class="abs phone-ring">
    <svg width="30" height="30" viewBox="0 0 30 30"><path d="M10 8c1-1 2-1 3 0l2 3c.5 1 0 1.5-.8 2.2-.6.5.5 2.3 1.5 3.3s2.8 2.1 3.3 1.5c.7-.8 1.2-1.3 2.2-.8l3 2c1 1 1 2 0 3-2 2-5 1.5-9-2.5S8 10 10 8z" fill="none" stroke="#0f3a70" stroke-width="1.6"/></svg>
  </div>
</header>

<section class="abs hero" role="img" aria-label="City skyline photograph tinted in brand blue">
  <h1 class="abs cond">ABOUT US</h1>
</section>

<h2 class="abs section-title cond">LEARN ABOUT WHO WE ARE</h2>
<div class="abs photo" role="img" aria-label="Photo of a man working on a laptop at the beach"></div>
<div class="abs intro">
  <p>Velmoro Wireless is at the forefront of revolutionising high-speed internet access (HSIA) services. We offer complete wireless solutions: Right from developing individual components such as hotspots and access controllers, to installation of the internet infrastructure. Once we setup the HSIA for our clients, we back it up with round-the-clock tech support.</p>
  <p>Velmoro's expertise in wireless technology has attracted a growing client base from all over Australia.</p>
</div>

<div class="abs feature" style="top:372px">
  <div class="feature-head">
    <div class="icon-circle"><svg width="24" height="20" viewBox="0 0 24 20"><path d="M2 7a14 14 0 0 1 20 0M5 10.5a9.5 9.5 0 0 1 14 0M8.5 14a4.5 4.5 0 0 1 7 0" fill="none" stroke="#fff" stroke-width="2" stroke-linecap="round"/><circle cx="12" cy="17" r="1.8" fill="#fff"/></svg></div>
    <h3 class="feature-title">An Emerging Leader in<br>Wireless Hotspots</h3>
  </div>
  <p>Our focus is on becoming the best service provider in the key category of wireless services. With high-speed broadband solutions for the hospitality industry, and mobile hotspots for remote locations, we endeavour to meet the rising demand of internet connectivity anywhere and everywhere.</p>
  <p>Velmoro currently manages over 2000 installations in various parts of the country. Clients employ our services to improve their existing IT infrastructure which enables them to provide a faster, more secure internet experience to their customers.</p>
</div>

<div class="abs feature" style="top:604px">
  <div class="feature-head">
    <div class="icon-circle"><svg width="22" height="22" viewBox="0 0 22 22"><path d="M6 2h10v6a5 5 0 0 1-10 0zM6 4H2c0 4 2 6 4 6M16 4h4c0 4-2 6-4 6M11 13v4M7 20h8" fill="none" stroke="#fff" stroke-width="2"/></svg></div>
    <h3 class="feature-title">Award-Winning Solutions</h3>
  </div>
  <p>In 2002, our tech experts developed a user-friendly, feature-rich software platform. Today, we deliver customised information systems based on the platform. Our robust, secure network requires minimal maintenance and can be monitored remotely from anywhere in the world.</p>
  <p>Velmoro's software platform is flexible and easy to configure. It can adapt to manual or automatic payment processing in a managed or self-regulated environment. We were awarded the National Telecom Users Forum (NTUF) award for Innovative Broadband Solution in recognition of our market-leading software platform.</p>
</div>

<div class="abs philosophy">
  <div class="feature-head">
    <div class="icon-circle"><svg width="22" height="22" viewBox="0 0 22 22"><path d="M20 2c-6 0-10 4-12 8l4 4c4-2 8-6 8-12zM8 10H4l-2 3 4 1M12 14v4l-3 2-1-4M6 16l-3 3" fill="none" stroke="#fff" stroke-width="1.8" stroke-linejoin="round"/></svg></div>
    <h3 class="feature-title">Premium Customer Service Is Our Business Philosophy</h3>
  </div>
  <p>All our efforts and expertise are geared towards one thing – providing a premium customer service experience. We are guided in our philosophy by a development team that provides clients with stable, secure wireless solutions. When hotel guests, staff, and customers log on to our network they experience an interface that they are familiar with. Users can browse, view media, and download apps without any fear of their personal information being compromised. Our wireless networks apply a combination of security measures for a secure internet experience.</p>
  <p>Velmoro wireless hotspots and broadband systems are providing laptop users with HSIA services in a variety of hospitality centres, convention centres, and recreation clubs around the country. The systems can be accessed with a wide range of payment options that include manually processed cash payments, automatic debit through card payment, and direct billing to the guest's room account with the client's Property Management System (PMS).</p>
  <p>the success we have achieved so far is based on our commitment to help clients develop and grow their business with expert solutions and premium customer service.</p>
</div>

<section class="abs statement" role="img" aria-label="Dark blurred photo of a person at a laptop">
  <h2 class="abs cond">VELMORO WIRELESS</h2>
  <p class="abs">has been a leader in wireless<br>networks and internet billing systems for over a decade.</p>
</section>

<section class="abs team">
  <h2 class="abs cond">OUR TEAM</h2>
  <div class="abs sub">The Superstars That Make Things Happen</div>
  <div class="abs rule"></div>

  <div class="abs card" style="left:98px">
    <div class="card-top" role="img" aria-label="Blue city skyline photo"></div>
    <svg class="card-cut" width="235" height="90" viewBox="0 0 235 90"><path d="M0 90L0 72 235 40 235 90z" fill="#fff"/></svg>
    <div class="avatar" role="img" aria-label="Portrait of team member"></div>
    <h3>Tom Harlow | MD</h3>
    <p>Lorem ipsum dolor sit amet, consectetur adipiscing elit, sed do eiusmod tempor incidi</p>
    <div class="socials"><span></span><span></span><span></span></div>
  </div>
  <div class="abs card" style="left:355px">
    <div class="card-top" role="img" aria-label="Blue city skyline photo"></div>
    <svg class="card-cut" width="235" height="90" viewBox="0 0 235 90"><path d="M0 90L0 72 235 40 235 90z" fill="#fff"/></svg>
    <div class="avatar" role="img" aria-label="Portrait of team member"></div>
    <h3>Tom Harlow | MD</h3>
    <p>Lorem ipsum dolor sit amet, consectetur adipiscing elit, sed do eiusmod tempor incidi</p>
    <div class="socials"><span></span><span></span><span></span></div>
  </div>
  <div class="abs card" style="left:612px">
    <div class="card-top" role="img" aria-label="Blue city skyline photo"></div>
    <svg class="card-cut" width="235" height="90" viewBox="0 0 235 90"><path d="M0 90L0 72 235 40 235 90z" fill="#fff"/></svg>
    <div class="avatar" role="img" aria-label="Portrait of team member"></div>
    <h3>Tom Harlow | MD</h3>
    <p>Lorem ipsum dolor sit amet, consectetur adipiscing elit, sed do eiusmod tempor incidi</p>
    <div class="socials"><span></span><span></span><span></span></div>
  </div>
  <div class="abs card" style="left:868px">
    <div class="card-top" role="img" aria-label="Blue city skyline photo"></div>
    <svg class="card-cut" width="235" height="90" viewBox="0 0 235 90"><path d="M0 90L0 72 235 40 235 90z" fill="#fff"/></svg>
    <div class="avatar" role="img" aria-label="Portrait of team member"></div>
    <h3>Tom Harlow | MD</h3>
    <p>Lorem ipsum dolor sit amet, consectetur adipiscing elit, sed do eiusmod tempor incidi</p>
    <div class="socials"><span></span><span></span><span></span></div>
  </div>
</section>

<section class="abs partners" aria-label="Clients">
  <div class="abs partner" style="left:97px"><span></span></div>
  <div class="abs partner" style="left:267px"><span></span></div>
  <div class="abs partner" style="left:437px"><span></span></div>
  <div class="abs partner" style="left:607px"><span></span></div>
  <div class="abs partner" style="left:777px"><span></span></div>
  <div class="abs partner" style="left:947px"><span></span></div>
</section>

<footer class="abs site-footer">
  <div class="abs foot-logo"><span class="logo-name">Velmoro</span><span class="logo-dot"></span></div>
  <div class="abs foot-social"><span></span><span></span><span></span><span></span></div>
  <div class="abs foot-links">
    <div class="foot-head cond">QUICK LINKS</div>
    <ul><li>CASE STUDIES</li><li>TESTIMONIALS</li><li>NEWS</li><li>RESELLERS</li></ul>
  </div>
  <div class="abs foot-contact">
    <div class="foot-head cond">CONTACT US</div>
    <div class="contact-row"><svg width="14" height="18" viewBox="0 0 14 18"><path d="M7 0a6 6 0 0 1 6 6c0 5-6 12-6 12S1 11 1 6a6 6 0 0 1 6-6z" fill="#fff"/><circle cx="7" cy="6" r="2.3" fill="#0e3c74"/></svg><span>Velmoro Wireless 42 Harbour Crescent<br>Coral Bay, QLD 4221</span></div>
    <div class="contact-row" style="font-size:16px"><svg width="16" height="16" viewBox="0 0 16 16"><path d="M3 1c1-1 2 0 3 1l1 2c.5 1-.5 1.5-1 2 .5 1.5 2.5 3.5 4 4 .5-.5 1-1.5 2-1l2 1c1 1 2 2 1 3-2 2-5 1-9-3S1 3 3 1z" fill="#fff"/></svg><span>1300 555 014</span></div>
    <div class="contact-row"><svg width="16" height="12" viewBox="0 0 16 12"><rect x=".8" y=".8" width="14.4" height="10.4" fill="none" stroke="#fff" stroke-width="1.5"/><path d="M1 1l7 6 7-6" fill="none" stroke="#fff" stroke-width="1.5"/></svg><span>sales@velmoro.com.au</span></div>
  </div>
  <div class="abs signup">
    <div class="foot-head cond">SIGN UP TO RECEIVE EMAIL</div>
    <div class="field">Enter Name</div>
    <div class="field email">Enter Email</div><div class="btn">SUBSCRIBE</div>
  </div>
</footer>
<div class="abs copyright">© 2015 Velmoro Wireless. All Rights Reserved.</div>

</body>
</html>
```